Making Maui's Gentle Reach of Kindness Open to Everyone and then add the logo Camp Brightfern Maui

We need a design to a brochure to promote building and seek donors of the first fully wheelchair accessible camp which would be located on Maui, HI and with a FOCUS on why it needs to be built.
We have a fundraiser on https://www.pledgeriver.example/education-fundraising/a-home-for-youth-with-disabilities-to-flourish--7/x/50391742 PLEASE SEE THE BRIEF FOR INFO

Target Market(s)

those with disabilities and their families, or anyone interested in fully accessible facility, rehabilitation after accident

Industry/Entity Type

Education

Requirements
Must have
• Please put in order in tri fold brochure
• Who we Are:
• The Board Members of Rising Tide Path are dedicated to the need of accessibility for outdoor activities within an educational camp facility. Our Board Members represent a variety of backgrounds, and disabilities.
• Our Mission:
• Rising Tide Path, Inc is a 501c(3) nonprofit founded in 2004 in Hawaii that is dedicated to helping children, young people and particularly those with mobility impairments reach their own potential, empower dignity, and motivate purposeful living. Our passion is to inspire, educate, and create accessible outdoor facilities.
• We have 5 beautiful acres of leased land located on the West sunny side of the Maui Island. This property is near an accessible part of the ocean
• The Need:
• 53 million individuals with disabilities live in the United States and one billion people with disabilities live around the world. Everyone in their life time is at risk of mobility impairment. This could happen any day, at anytime to anyone. Families that experience catastrophic events or individuals are born with developmental disabilities face enormous challenges. Many families that experience this are financially destroyed and spiritually as well as emotionally exhausted. One of the biggest struggles those with disabilities face is getting enough education. Most individuals with disabilities often are left to feel isolated and alone. The American Disabilities Act was implemented in 1990, but most therapeutic outdoor activities are not accessible to those with disabilities especially on the Hawaiian Islands.
• Building the dream:
• Camp Brightfern Maui will be a 100% wheelchair accessible and barrier free camp facility that will be built on 5 acres of land in Olowalu, Maui Hawaii. This future farm facility would be used to educate, and enrich the lives of those with disabilities as well as their families and help them heal their emotional, spiritual, and psychological hurt. In an ranch like setting, educational and nurturing programs will be centered around old Hawaiian culture, agricultural history, production, animal care, and teamwork. With a host of innovations for enhanced accessibility such as raised garden beds, and wider pathways those attending the facility would be empowered with more independence. Therapeutic adaptive sporting activities designed for those with physical mobility impairments will be available, like kayaking, paddle boarding, and zip lining.
• Life Time Value:
• This future facility would promote awareness to the community around it about the importance of humanity and education as well as providing inclusion and equality for those with disabilities. Therapeutic outdoor activities will allow those to heal and gain invaluable tools. Participants of the camp would leave with a Rising Tide Path Attitude, integrating into their communities with positive potential and purposeful living. Together we can walk and roll!
• Where your money will go:
• Phase 1 to pursue a State Special Land Use permit.
• To get the special land use permit together for the Planning Department of Maui, it will cost $20,000.
• Below is a breakdown of the first phase of the permit:
• -Archaeological summary
• -Site survey
• -fulfill legal notification requirements to existing neighbors
• -Traffic Impact analysis
• -Drainage and Erosion Control analysis
• -Waste Water System Design
• -Topographical Design Survey
• -Construction Permitting Phase
• We Need Your Help:
• Join us in this amazing mission by becoming a member of our Rising Tide Path team. You will leave a legacy of Maui’s first 100% accessible camp.
• A) Ambassador- help spread the word
• B) Build the camp- grab a shovel swing a hammer
• C) Contribute financially
• D) Donate materials and services
• Help support the dream by buying a camp logo t-shirt on CampBrightfernmaui.example
• Rising Tide Path
• PO BOX 418
• Albany, OR 97321
• 541-555-0173
• CampBrightfernMaui@mailbox.example
• Please include this in someway, like an QR scan or something https://www.pledgeriver.example/education-fundraising/a-home-for-youth-with-disabilities-to-flourish--7
Nice to have
• Things we would like- kids at a campfire someone in a wheelchair there laughing
Should not have
• NO photos of Dale Vorsting unless its the one of him and the waterfall phone number 541-555-0148 or trekfieldhollow@mailbox.example these are both wrong contact info

```html
<!DOCTYPE html>
<html lang="en">
<head>
<meta charset="utf-8">
<title>Camp Brightfern Maui – Brochure</title>
<link rel="stylesheet" href="https://fonts.googleapis.com/css2?family=Crimson+Pro:wght@400;600;700&family=Lato:wght@400;700&display=swap">
<style>
  :root {
    --navy: #1b3d7a;
    --deep-blue: #1d5fae;
    --sky-blue: #1e8bd3;
    --bright-blue: #2a9ae0;
    --sun-yellow: #f3bd1c;
    --cream: #fbf6e8;
    --brown: #6b4a1f;
    --ink: #2b2b2b;
    --white: #ffffff;
    --backdrop: #e4e4e4;
  }
  * { box-sizing: border-box; margin: 0; padding: 0; }
  html, body { width: 1200px; height: 848px; overflow: hidden; }
  body { background: var(--backdrop); font-family: "Lato", sans-serif; position: relative; }

  .page { position: absolute; top: 46px; width: 532px; height: 748px; overflow: hidden; background: var(--cream); }
  .page--front { left: 50px; }
  .page--back { left: 612px; }
  .page > * { position: absolute; }
  .shapes { left: 0; top: 0; width: 532px; height: 748px; }

  /* Front page */
  .hero-photo { left: 0; top: 0; width: 532px; height: 330px;
    background: linear-gradient(180deg, #c9a93a 0%, #8c8a3c 30%, #6a4a8a 55%, #b8923a 80%, #d9b25a 100%); }
  .brand-seal { left: 300px; top: 278px; width: 208px; height: 208px; border-radius: 50%;
    background: var(--white); border: 5px solid var(--brown);
    display: flex; flex-direction: column; align-items: center; justify-content: center; }
  .brand-name { font-family: "Crimson Pro", serif; font-weight: 600; color: var(--brown);
    text-align: center; line-height: 1.05; letter-spacing: 0.5px; white-space: nowrap; }
  .brand-seal .brand-name { font-size: 21px; }
  .tagline { left: 21px; top: 322px; font-family: "Crimson Pro", serif; line-height: 1; }
  .tagline__lead { display: block; font-size: 30px; color: #111; font-weight: 600; }
  .tagline__accent { display: block; font-size: 35px; color: var(--sky-blue); font-weight: 700; margin-top: 6px; }
  .tagline__strong { display: block; font-size: 50px; color: var(--navy); font-weight: 700; margin-top: 4px; }
  .intro { left: 26px; top: 484px; width: 205px; font-size: 13px; line-height: 1.27; color: var(--ink); }
  .camp-title { right: 26px; top: 504px; text-align: right; font-family: "Crimson Pro", serif;
    color: var(--white); font-weight: 600; line-height: 1; text-shadow: 1px 2px 2px rgba(0,0,0,0.35); white-space: nowrap; }
  .camp-title span { display: block; }
  .camp-title__top { font-size: 33px; }
  .camp-title__bottom { font-size: 56px; margin-top: 4px; }
  .funding-note { left: 212px; top: 614px; width: 294px; font-size: 13px; line-height: 1.25;
    color: var(--white); text-align: justify; text-align-last: right; }
  .inset-photo { left: 18px; top: 553px; width: 168px; height: 168px; border-radius: 50%;
    border: 5px solid var(--brown);
    background: radial-gradient(circle at 45% 50%, #7a8f9a 0%, #4a5a68 55%, #2f3b44 100%); }
  .site-url { left: 0; top: 716px; width: 532px; text-align: center; font-size: 14px;
    letter-spacing: 2px; color: var(--navy); font-weight: 700; }

  /* Back page */
  .care-photo { left: 0; top: 0; width: 532px; height: 205px;
    background: linear-gradient(100deg, #e8e6e2 0%, #d9c8c4 35%, #efe9e6 60%, #cfd6dd 100%); }
  .badge { left: 340px; top: 52px; width: 176px; height: 176px; }
  .badge__text { left: 350px; top: 78px; width: 156px; text-align: center; font-family: "Crimson Pro", serif;
    font-weight: 700; color: var(--white); font-size: 31px; line-height: 1.3; }
  .section-title { left: 20px; font-family: "Crimson Pro", serif; font-weight: 600;
    color: var(--sun-yellow); font-size: 22px; }
  .section-title--mission { top: 212px; }
  .section-title--story { top: 332px; }
  .mission-text { left: 20px; top: 249px; width: 488px; font-size: 10.4px; line-height: 1.24;
    color: var(--white); text-align: justify; }
  .story-text { left: 20px; top: 370px; width: 290px; font-size: 10.4px; line-height: 1.24;
    color: var(--white); text-align: justify; }
  .story-photo { left: 322px; top: 369px; width: 190px; height: 92px; border-radius: 7px;
    border: 4px solid var(--white);
    background: linear-gradient(90deg, #8a8a8a 0%, #5a5a5a 48%, #b8765a 52%, #6e3a2a 100%); }
  .promise { right: 22px; top: 500px; text-align: right; font-family: "Crimson Pro", serif;
    font-weight: 700; color: var(--navy); font-size: 22px; line-height: 1.42; white-space: nowrap;
    text-shadow: -1px -1px 0 #fff, 1px -1px 0 #fff, -1px 1px 0 #fff, 1px 1px 0 #fff, 2px 2px 2px rgba(0,0,0,0.3); }
  .promise span { display: block; }
  .site-facts { right: 22px; top: 568px; font-family: "Crimson Pro", serif; font-weight: 600;
    color: var(--navy); font-size: 13.5px; white-space: nowrap; }
  .plan-view { width: 120px; height: 120px; border-radius: 50%; border: 5px solid var(--navy);
    top: 596px; }
  .plan-view--site { left: 260px; background: radial-gradient(circle, #eef3ea 0%, #c9dcc0 60%, #f2f4f0 100%); }
  .plan-view--floor { left: 388px; background: radial-gradient(circle, #ffffff 0%, #eceef2 70%, #dfe3ea 100%); }
  .back-brand { left: 30px; top: 664px; display: flex; align-items: center; gap: 10px; }
  .back-brand .brand-name { font-size: 20px; }
  .brand-dot { width: 18px; height: 18px; border-radius: 50%; background: var(--sun-yellow); flex: none; }
</style>
</head>
<body>

<section class="page page--front">
  <div class="hero-photo" role="img" aria-label="Photo: a family walking through an autumn park, pushing a smiling child in a wheelchair"></div>
  <svg class="shapes" viewBox="0 0 532 748" aria-hidden="true">
    <path d="M0,300 C180,292 380,272 532,236 L532,748 L0,748 Z" fill="var(--cream)"/>
    <path d="M0,300 C180,292 380,272 532,236" fill="none" stroke="var(--deep-blue)" stroke-width="9"/>
    <path d="M0,316 C180,308 380,288 532,252" fill="none" stroke="var(--sun-yellow)" stroke-width="14"/>
    <path d="M0,620 C110,612 230,525 330,455 C400,405 470,392 532,384 L532,710 L0,710 Z" fill="var(--sky-blue)"/>
    <path d="M110,665 C190,595 270,515 360,452" fill="none" stroke="var(--deep-blue)" stroke-width="12"/>
    <path d="M150,690 C230,620 310,540 400,480" fill="none" stroke="var(--deep-blue)" stroke-width="7" opacity="0.7"/>
    <rect x="0" y="710" width="532" height="38" fill="var(--cream)"/>
  </svg>
  <div class="brand-seal"><p class="brand-name">CAMP BRIGHTFERN<br>MAUI</p></div>
  <h1 class="tagline">
    <span class="tagline__lead">A place for children</span>
    <span class="tagline__accent">with disabilities</span>
    <span class="tagline__strong">to THRIVE</span>
  </h1>
  <p class="intro">Providing the tools of success for individuals with disabilities in an educational outdoor school setting.</p>
  <h2 class="camp-title"><span class="camp-title__top">Camp Brightfern</span><span class="camp-title__bottom">Maui</span></h2>
  <p class="funding-note">We have 5 acres of land now we are waiting to have funds to create an environment where those with disabilities are encouraged to expand and explore new possibilities</p>
  <div class="inset-photo" role="img" aria-label="Photo: a caregiver helping a child seated in a wheelchair outdoors"></div>
  <p class="site-url">www.pledgeriver.example</p>
</section>

<section class="page page--back">
  <div class="care-photo" role="img" aria-label="Photo: a smiling woman pushing a girl in a wheelchair down a bright hallway"></div>
  <svg class="shapes" viewBox="0 0 532 748" aria-hidden="true">
    <defs>
      <linearGradient id="backBlue" x1="0" y1="0" x2="0" y2="1">
        <stop offset="0" stop-color="var(--bright-blue)"/>
        <stop offset="1" stop-color="#1473bf"/>
      </linearGradient>
    </defs>
    <path d="M0,196 C150,186 320,150 532,118 L532,748 L0,748 Z" fill="url(#backBlue)"/>
    <path d="M180,190 C300,175 420,150 532,128" fill="none" stroke="var(--sun-yellow)" stroke-width="5"/>
    <path d="M0,556 C160,550 340,548 532,540 L532,748 L0,748 Z" fill="var(--cream)"/>
    <path d="M0,550 C170,544 350,542 532,534" fill="none" stroke="var(--sun-yellow)" stroke-width="5"/>
    <path d="M230,748 C290,650 390,600 532,580 L532,748 Z" fill="var(--deep-blue)"/>
    <path d="M300,748 C360,680 440,632 532,616" fill="none" stroke="var(--sun-yellow)" stroke-width="7"/>
  </svg>
  <svg class="badge" viewBox="-88 -88 176 176" aria-hidden="true">
    <polygon transform="scale(1.12)" fill="var(--sun-yellow)" points="76,0 62.8,12.5 70.2,29.1 53.2,35.6 53.7,53.7 35.6,53.2 29.1,70.2 12.5,62.8 0,76 -12.5,62.8 -29.1,70.2 -35.6,53.2 -53.7,53.7 -53.2,35.6 -70.2,29.1 -62.8,12.5 -76,0 -62.8,-12.5 -70.2,-29.1 -53.2,-35.6 -53.7,-53.7 -35.6,-53.2 -29.1,-70.2 -12.5,-62.8 0,-76 12.5,-62.8 29.1,-70.2 35.6,-53.2 53.7,-53.7 53.2,-35.6 70.2,-29.1 62.8,-12.5"/>
    <polygon fill="var(--deep-blue)" points="76,0 62.8,12.5 70.2,29.1 53.2,35.6 53.7,53.7 35.6,53.2 29.1,70.2 12.5,62.8 0,76 -12.5,62.8 -29.1,70.2 -35.6,53.2 -53.7,53.7 -53.2,35.6 -70.2,29.1 -62.8,12.5 -76,0 -62.8,-12.5 -70.2,-29.1 -53.2,-35.6 -53.7,-53.7 -35.6,-53.2 -29.1,-70.2 -12.5,-62.8 0,-76 12.5,-62.8 29.1,-70.2 35.6,-53.2 53.7,-53.7 53.2,-35.6 70.2,-29.1 62.8,-12.5"/>
  </svg>
  <p class="badge__text">LIFE<br>TIME<br>VALUE</p>

  <h3 class="section-title section-title--mission">Our Mission :</h3>
  <p class="mission-text">Rising Tide Path, Inc is a 501c(3) nonprofit founded in 2004 that is dedicated to helping children, young people and particularly those with mobility impairments reach their own potential, empower dignity, and motivate purposeful living. To build and operate fully wheelchair-accessible camp facilities, these barrier-free camps will give individuals and families, particularly children, the youth and those with mobility impairments or other disabilities the opportunity to experience, enjoy and learn tools to thrive in life and go past the limitations often looming when faced with dependency.</p>

  <h3 class="section-title section-title--story">A Real Story :</h3>
  <p class="story-text">Dale Vorsting broke his neck in a surfing accident just before his 18th birthday, and became paralyzed from the neck down. Empowered by his own limitations he had a choice to give up or go on. With a positive attitude he accomplished a Master's Degree in Social Work, became a nationally known Motivational Speaker, author, mouth painter, drove a Skyrunner Corvane 100mph after his accident with only the use of his teeth, and most importantly dedicated father of 2 daughters.</p>
  <div class="story-photo" role="img" aria-label="Photos: a young athlete before his accident and later painting with a brush held in his mouth"></div>

  <p class="promise"><span>Camp Brightfern Maui will be a 100%</span><span>wheelchair accessible and barrier free camp</span></p>
  <p class="site-facts">Facility on 5 acres of land in Olowalu, Maui Hawaii</p>

  <div class="plan-view plan-view--site" role="img" aria-label="Site plan drawing of the 5 acre camp grounds"></div>
  <div class="plan-view plan-view--floor" role="img" aria-label="Floor plan drawing of the camp cabins"></div>

  <div class="back-brand"><span class="brand-dot"></span><p class="brand-name">CAMP BRIGHTFERN<br>MAUI</p></div>
</section>

</body>
</html>
```